Trovadel Ltda

Logo design focused on: - Construction of civil works - Electrical services - Metal structures - Equipment rental Tomas Ibarra Luque Manager trovadel.ltda@norvexmail.com 56 9 41827035 Quirobamba s / n, Tolvas, San Pedro de Atacama

Target Market(s)

Building

Colors
33a6d7
0292cd
33b8a4
0555a3

```html
<!DOCTYPE html>
<html lang="es">
<head>
<meta charset="utf-8">
<title>Trovadel Ltda – Tarjeta de presentación</title>
<link href="https://fonts.googleapis.com/css2?family=Rubik:wght@300;400;500;700&display=swap" rel="stylesheet">
<style>
  :root {
    --sky: #33a6d7;
    --azure: #0292cd;
    --teal: #33b8a4;
    --band: #17b0b8;
    --navy: #0555a3;
    --paper: #ffffff;
    --backdrop: #e6e8ec;
    --watermark: #eef3f5;
  }
  * { margin: 0; padding: 0; box-sizing: border-box; }
  html, body {
    width: 1200px; height: 1076px; overflow: hidden;
    background: var(--backdrop);
    font-family: "Rubik", sans-serif;
  }
  .card {
    position: absolute; left: 100px; top: 260px;
    width: 1000px; height: 556px;
    background: var(--paper);
    overflow: hidden;
    box-shadow: 0 10px 30px rgba(0,0,0,0.12);
  }
  .card__backdrop-mark {
    position: absolute; right: -90px; top: 60px;
    width: 440px; height: 440px; border-radius: 50%;
    background: var(--watermark);
  }
  .brand {
    position: absolute; left: 48px; top: 52px;
    display: flex; align-items: center; gap: 22px;
  }
  .brand__dot {
    width: 92px; height: 92px; border-radius: 50%;
    background: var(--azure);
  }
  .brand__rule { width: 2px; height: 100px; background: var(--azure); }
  .brand__name {
    font-size: 50px; font-weight: 400; color: var(--navy);
    letter-spacing: 2px;
  }
  .person { position: absolute; left: 48px; top: 205px; }
  .person__name {
    font-size: 38px; font-weight: 300; color: var(--band);
    text-transform: uppercase; letter-spacing: 1px;
  }
  .person__role {
    font-size: 24px; font-weight: 700; color: var(--navy);
    text-transform: uppercase; margin-top: 2px;
  }
  .contact {
    position: absolute; right: 44px; top: 250px;
    text-align: right;
  }
  .contact__address {
    font-size: 25px; font-weight: 400; color: var(--navy);
    text-transform: uppercase; letter-spacing: 1px; line-height: 1.35;
  }
  .contact__line {
    font-size: 25px; font-weight: 300; color: var(--band);
    line-height: 1.4;
  }
  .contact__address + .contact__line { margin-top: 30px; }
  .services {
    position: absolute; left: 0; right: 0; top: 440px; height: 52px;
    background: var(--band);
    display: flex; align-items: center; justify-content: center;
    color: var(--paper); font-size: 21px; font-weight: 300;
    white-space: nowrap;
  }
</style>
</head>
<body>
  <article class="card">
    <div class="card__backdrop-mark" aria-hidden="true"></div>

    <header class="brand">
      <span class="brand__dot" aria-hidden="true"></span>
      <span class="brand__rule" aria-hidden="true"></span>
      <span class="brand__name">TROVADEL Ltda</span>
    </header>

    <section class="person">
      <p class="person__name">Tomas Ibarra Luque</p>
      <p class="person__role">Gerente</p>
    </section>

    <section class="contact">
      <p class="contact__address">Quirobamba S/N, Tolvas<br>San Pedro de Atacama</p>
      <p class="contact__line">trovadel.ltda@norvexmail.com</p>
      <p class="contact__line">+56 9 41827035</p>
    </section>

    <footer class="services">Construcción de Obras Civiles-Servicios eléctricos-Estructuras metálicas-Arriendo de Equipos</footer>
  </article>
</body>
</html>
```